Business cards

Looking for business cards. Brackett Diesel Performance is the name.
Business colors are a hunter or forest green(either green could be used) with silver writing and logo.
Would like it to say maintenance, repairs and motor work, specializing in Torvalen, glideforge and Halvors diesels somewhere on the card. Probably on the back
Phone number is
Marek
555-302-4816
Picture attached is the current logo and is on shirts and hoodies. I would prefer that on the front of the card
Looking for business cards. Brackett Diesel Performance is the name. Business colors are a hunter or forest green(either green could be used) with silver writing and logo. Would like it to say maintenance, repairs and motor work, specializing in Torvalen, glideforge and Halvors diesels somewhere on the card. Probably on the back Phone number is Marek 555-302-4816 Picture attached is the current logo and is on shirts and hoodies. I would prefer that on the front of the card

```html
<!DOCTYPE html>
<html lang="en">
<head>
<meta charset="utf-8">
<title>Brackett Diesel Performance – Business Cards</title>
<link href="https://fonts.googleapis.com/css2?family=Poppins:wght@300;400;600&family=Kaushan+Script&display=swap" rel="stylesheet">
<style>
  :root {
    --backdrop: #777777;
    --card-white: #ffffff;
    --forest: #228b22;
    --silver: #e2e2e2;
    --shadow: rgba(0, 0, 0, 0.85);
  }
  html, body {
    margin: 0;
    padding: 0;
    width: 1065px;
    height: 1200px;
    overflow: hidden;
    background: var(--backdrop);
  }
  .sheet {
    position: relative;
    width: 1065px;
    height: 1200px;
  }
  .card {
    position: absolute;
    width: 583px;
    height: 363px;
    filter: drop-shadow(3px 3px 2px var(--shadow));
  }
  .card-front {
    left: 292px;
    top: 218px;
    background: var(--card-white);
    border-radius: 0 181.5px 181.5px 0;
  }
  .card-back {
    left: 262px;
    top: 623px;
    background: var(--forest);
    border-radius: 181.5px 0 0 181.5px;
  }
  .brand {
    position: absolute;
    left: 60px;
    top: 105px;
    width: 225px;
    height: 175px;
    display: flex;
    flex-direction: column;
    align-items: center;
    justify-content: center;
    font-family: "Poppins", sans-serif;
    font-weight: 600;
    color: var(--forest);
    text-align: center;
    line-height: 1.15;
    font-size: 30px;
  }
  .brand .brand-sub {
    font-size: 24px;
  }
  .divider {
    position: absolute;
    left: 340px;
    top: 112px;
    width: 1px;
    height: 173px;
    background: var(--forest);
  }
  .contact {
    position: absolute;
    left: 368px;
    top: 154px;
    color: var(--forest);
  }
  .contact-name {
    font-family: "Kaushan Script", cursive;
    font-size: 33px;
    line-height: 1;
    margin: 0;
  }
  .contact-phone {
    font-family: "Poppins", sans-serif;
    font-weight: 300;
    font-size: 16.5px;
    letter-spacing: 0.4px;
    margin: 6px 0 0 2px;
  }
  .services {
    position: absolute;
    left: 0;
    right: 0;
    top: 148px;
    margin: 0;
    padding: 0;
    list-style: none;
    text-align: center;
    font-family: "Poppins", sans-serif;
    font-weight: 400;
    font-size: 23.5px;
    line-height: 32px;
    color: var(--silver);
  }
  .services li {
    padding-left: 24px;
  }
</style>
</head>
<body>
<main class="sheet">
  <section class="card card-front" aria-label="Card front">
    <div class="brand">
      <span class="brand-name">Brackett</span>
      <span class="brand-sub">Diesel Performance</span>
    </div>
    <div class="divider"></div>
    <div class="contact">
      <p class="contact-name">Marek</p>
      <p class="contact-phone">555-302-4816</p>
    </div>
  </section>

  <section class="card card-back" aria-label="Card back">
    <ul class="services">
      <li>Maintenance</li>
      <li>Repairs and motor work</li>
      <li>Specializing in Torvalen</li>
      <li>Glideforge and Halvors diesels</li>
    </ul>
  </section>
</main>
</body>
</html>
```